Webpages for Sammalkivi Software Consulting

Needed: Webpage design.
Details:
One page site with good looking fonts and simple modern design. Logo would also be nice.
Page is for Software consulting company called: "Sammalkivi Software Consulting". Sammalkivi is my surname.
Pages should tell viewer that the company is reliable and its employees are hard-core professionals.
Company currently has one employee, that's me. So what I do is what this company does. I am software consultant. Basicly that means that I do Java/JavaEE/Web programming as subcontractor.
Here is more detail information about me.
SPECIALTIES
- Enterprise J2EE Application Programming and Architectures,
- Web development and
- Agile development.
I have over a decade of experience on designing and creating Java based web-services and applications to multiple interfaces. I also have plenty of experience about software architectures, design patterns and integration into third party systems. I’ve got good knowledge about agile software development and testing processes and I am experienced ScrumMaster and software project leader.
Target Market(s)
IT Businesses, Coding companies... Anyone who is buying coding as service.
Industry/Entity Type
Software

```html
<!DOCTYPE html>
<html lang="en">
<head>
<meta charset="utf-8">
<title>Sammalkivi Software Consulting</title>
<link href="https://fonts.googleapis.com/css2?family=Titillium+Web:wght@400&family=Noto+Sans:wght@400&display=swap" rel="stylesheet">
<style>
  :root {
    --heading-grey: #555;
    --title-grey: #666;
    --sub-grey: #aaa;
    --body-grey: #6a6a6a;
    --footer-grey: #c4c4c4;
    --rule: #cfcfcf;
    --header-top: #f8f8f8;
    --header-bottom: #efefef;
    --icon-grey: #9a9a9a;
  }
  * { margin: 0; padding: 0; box-sizing: border-box; }
  html, body { width: 1200px; height: 900px; overflow: hidden; background: #fff; }
  body { font-family: "Noto Sans", sans-serif; color: var(--body-grey); }

  .site-header {
    height: 81px;
    background: linear-gradient(180deg, var(--header-top), var(--header-bottom));
    border-bottom: 1px solid #dcdcdc;
    position: relative;
    overflow: hidden;
  }
  .site-header::after {
    content: "";
    position: absolute;
    left: 520px; top: -260px;
    width: 380px; height: 340px;
    border-radius: 50%;
    background: radial-gradient(circle, rgba(255,255,255,.7), rgba(255,255,255,0) 70%);
  }
  .wordmark {
    position: absolute; left: 189px; top: 27px;
    font-family: "Titillium Web", sans-serif;
    font-size: 20px; letter-spacing: .2px;
    color: var(--heading-grey); text-transform: uppercase;
    line-height: 28px; z-index: 1;
  }

  .page { width: 820px; margin: 0 auto; }
  .hero { text-align: center; padding-top: 99px; height: 259px; }
  .hero h1 {
    font-family: "Titillium Web", sans-serif; font-weight: 400;
    font-size: 31px; line-height: 40px; color: var(--title-grey);
  }
  .hero p {
    font-family: "Titillium Web", sans-serif;
    font-size: 20px; line-height: 28px; color: var(--sub-grey);
  }

  .rule { border-top: 1px dotted var(--rule); }

  .columns { display: flex; padding-top: 38px; height: 250px; }
  .col h2 {
    font-family: "Titillium Web", sans-serif; font-weight: 400;
    font-size: 21px; line-height: 28px; color: var(--heading-grey);
    margin-bottom: 8px;
  }
  .about { width: 420px; }
  .about-text { column-count: 2; column-gap: 20px; width: 400px; }
  .about-text, .col li { font-size: 11px; line-height: 20px; }
  .services { width: 210px; }
  .services ul { list-style: none; }
  .services li { padding-left: 20px; margin-bottom: 10px; position: relative; }
  .services li::before {
    content: ""; position: absolute; left: 9px; top: 7px;
    border-left: 3px solid var(--body-grey);
    border-top: 3px solid transparent; border-bottom: 3px solid transparent;
  }
  .contact { width: 190px; }
  .contact ul { list-style: none; }
  .contact li { position: relative; padding-left: 23px; margin-bottom: 10px; }
  .contact svg { position: absolute; left: 0; top: 2px; width: 16px; height: 16px; fill: var(--icon-grey); }

  .site-footer {
    display: flex; justify-content: space-between;
    padding-top: 6px; font-size: 11px; letter-spacing: .2px;
    text-transform: uppercase; color: var(--footer-grey);
  }
</style>
</head>
<body>
<header class="site-header">
  <div class="wordmark">Sammalkivi Software Consulting</div>
</header>

<main class="page">
  <section class="hero">
    <h1>Enterprise J2EE Application Programming and Architectures</h1>
    <p>+ web development &amp; agile development</p>
  </section>

  <div class="rule"></div>

  <section class="columns">
    <div class="col about">
      <h2>About</h2>
      <p class="about-text">Morbi malesuada, magna sit amet eleifend accumsan, quam massa egestas leo, id aliquam quam erat sit amet magna. Pellentesque quis elit et velit tincidunt sollicitu­din id vel magna. Proin vitae elit magna, sit amet aliquam felis. Donec rutrum pharetra hendrerit. In scelerisque congue convallis. Etiam iaculis, est et dignissim gravida, ante arcu ullamcorper quam, eu molestie dui.</p>
    </div>
    <div class="col services">
      <h2>What we do</h2>
      <ul>
        <li>Pellentesque quis elit</li>
        <li>Et velit tincidunt sollicitudin id</li>
        <li>Vel magna proin</li>
        <li>Vitae elit magna sit</li>
      </ul>
    </div>
    <div class="col contact">
      <h2>Contact</h2>
      <ul>
        <li><svg viewBox="0 0 16 16" aria-hidden="true"><path d="M1 4h14v9H1z M1 4l7 5 7-5" fill="none" stroke="#9a9a9a" stroke-width="1.4"/><path d="M1 4h14L8 9z"/></svg>olli@samsoco.fi</li>
        <li><svg viewBox="0 0 16 16" aria-hidden="true"><path d="M1 7c0-3 3-4 7-4s7 1 7 4l-3 1-1-2H5L4 8z"/><path d="M4 9h8l2 5H2z"/></svg>123.123.123</li>
        <li><svg viewBox="0 0 16 16" aria-hidden="true"><path d="M8 1l7 7h-2v7H9v-4H7v4H3V8H1z"/></svg>Foo Street 123<br>21435 Place, Finland</li>
      </ul>
    </div>
  </section>

  <div class="rule"></div>

  <footer class="site-footer">
    <span>Copyright 2011 Sammalkivi Software Consulting</span>
    <span>olli@samsoco.fi</span>
  </footer>
</main>
</body>
</html>
```